New website template

Create a new website template based on original logo and company vision.

The ideal outcome would be a PSD containing a home page and a content page.

The domain name is harbour-vale-works.co.uk and as you can see currently has a really simple holding page.

The company specialise in commercial property project management and have over 25 years experience in doing so.

Their logo is really simple, it would be nice to keep their site simple, clean, fresh and friendly.

We're planning to use bootstrap to ensure the site works nicely on a mobile device so it would be good if this could be kept in mind when designing the site.

Target Market(s)

commercial property sector.

Industry/Entity Type

It Company

Number of Pages Required

2 page

Font styles to use
Sans Serif

Colors
fece3e

Requirements
Must have
• a home page and a content page.
• bootstrap must be kept in mind when doing the design
• clean, fresh and professional
Should not have
• cartoon graphics.

```html
<!DOCTYPE html>
<html lang="en">
<head>
<meta charset="utf-8">
<title>Harbour Vale Works Ltd – Home</title>
<link rel="stylesheet" href="https://fonts.googleapis.com/css2?family=Open+Sans:wght@300;400&display=swap">
<style>
  :root {
    --brand-yellow: #fcf074;
    --ink: #222222;
    --body-text: #333333;
    --panel-grey: #f2f2f2;
    --white: #ffffff;
    --header-glass: rgba(255, 255, 255, 0.86);
    --line: #333333;
  }
  * { box-sizing: border-box; margin: 0; padding: 0; }
  html, body { width: 1200px; height: 733px; overflow: hidden; }
  body {
    position: relative;
    background: var(--panel-grey);
    font-family: "Open Sans", Arial, sans-serif;
    color: var(--body-text);
  }

  .site-header {
    position: absolute; left: 0; top: 0; width: 1200px; height: 48px;
    background: var(--header-glass); z-index: 3;
  }
  .brand-name {
    position: absolute; left: 21px; top: 13px;
    font-size: 15.5px; line-height: 22px; color: var(--ink); font-weight: 400;
  }
  .main-nav a {
    position: absolute; top: 9px; width: 80px; height: 28px;
    border: 1px solid var(--line); background: var(--white);
    font-size: 13.5px; color: var(--ink); text-decoration: none;
    display: flex; align-items: center; justify-content: center;
  }
  .main-nav a.is-active { background: var(--brand-yellow); border-color: #b8a93a; }

  .hero {
    position: absolute; left: 242px; top: 0; width: 958px; height: 560px;
    background: linear-gradient(180deg, #e9ecee 0%, #d9dcdc 28%, #7f8e6a 55%, #585b58 70%, #4a4b4a 100%);
  }
  .hero-callout {
    position: absolute; left: 855px; top: 245px; width: 322px; height: 110px;
    background: var(--white); padding: 6px 10px 0 10px; z-index: 2;
  }
  .hero-callout h2 { font-weight: 400; font-size: 27px; line-height: 1.2; color: #111; }
  .hero-callout p { font-size: 16.3px; line-height: 1.3; color: #111; margin-left: 5px; margin-top: 2px; }
  .hero-callout .btn { position: absolute; right: 0; bottom: 0; }

  .btn {
    display: inline-flex; align-items: center; justify-content: center;
    background: var(--brand-yellow); color: var(--ink); text-decoration: none;
    font-size: 13px; height: 21px; padding: 0 9px;
  }

  .welcome { position: absolute; left: 21px; top: 108px; width: 206px; }
  .section-title { font-weight: 300; font-size: 27px; color: var(--ink); letter-spacing: 0.3px; line-height: 1.2; }
  .welcome p, .welcome li {
    font-weight: 300; font-size: 12px; line-height: 16.5px; color: var(--ink);
  }
  .welcome p { margin-top: 4px; }
  .welcome p:first-of-type { margin-top: 6px; }
  .welcome ul { list-style: none; margin-top: 12px; }
  .welcome li { margin-bottom: 5.5px; padding-left: 8px; text-indent: -8px; }
  .welcome .btn { margin-top: 17px; height: 28px; width: 87px; font-size: 12.5px; }

  .contact { position: absolute; left: 21px; top: 572px; }
  .contact .section-title, .featured .section-title { font-size: 22px; }
  .contact address { font-style: normal; font-weight: 300; font-size: 12px; line-height: 15.5px; color: var(--ink); margin-top: 2px; }
  .contact .lines { margin-top: 15px; }

  .featured { position: absolute; left: 242px; top: 572px; width: 935px; }
  .view-more {
    position: absolute; right: 0; top: 10px; font-size: 12.5px; color: var(--ink);
    text-decoration: underline; text-underline-offset: 3px;
  }
  .project-strip { position: absolute; top: 44px; left: 0; display: flex; gap: 22.5px; }
  .project-thumb { width: 114px; height: 70px; }
  .thumb-1 { background: linear-gradient(180deg, #cfd3d5, #6e7a5a); }
  .thumb-2 { background: linear-gradient(180deg, #e3e5e6 0%, #c8ccca 55%, #6c7268 100%); }
  .thumb-3 { background: linear-gradient(180deg, #b9cde0 0%, #8a7a5a 55%, #6e5a4c 100%); }
  .thumb-4 { background: linear-gradient(180deg, #e6e8ea 0%, #a8493a 45%, #55504c 100%); }
  .thumb-5 { background: linear-gradient(180deg, #e4e6e8 0%, #c9ccc8 50%, #5d6a4d 100%); }
  .thumb-6 { background: linear-gradient(180deg, #d8dde2 0%, #8a5a44 50%, #6c5c50 100%); }
  .thumb-7 { background: linear-gradient(180deg, #cfd6de 0%, #a04f3e 45%, #7b4636 100%); }

  .copyright { position: absolute; right: 23px; top: 702px; font-size: 12px; font-weight: 300; color: var(--ink); }
</style>
</head>
<body>
  <header class="site-header">
    <span class="brand-name">Harbour Vale Works Ltd.</span>
    <nav class="main-nav">
      <a class="is-active" href="#" style="left:677px">Home</a>
      <a href="#" style="left:780px">About Us</a>
      <a href="#" style="left:887px">Projects</a>
      <a href="#" style="left:989px">Clients</a>
      <a href="#" style="left:1097px">Contact Us</a>
    </nav>
  </header>

  <div class="hero" role="img" aria-label="Photograph of a steel lattice sculpture framing a white apartment block, lawn and paved courtyard"></div>

  <aside class="hero-callout">
    <h2>‘It’s all about Attitude’</h2>
    <p>Lorem Ipsum is simply dummy text of the printing and typesetting industry.</p>
    <a class="btn" href="#">Read More</a>
  </aside>

  <section class="welcome">
    <h1 class="section-title">WELCOME</h1>
    <p>Harbour Vale Works Ltd is a project management company that embraces a modern philosophy based on 40 years of in-house and consultancy client experience and expertise; latter&shy;ly with involvement with a number of high end London projects.</p>
    <p>Harbour Vale Works is client-focused.</p>
    <p>Prior to forming Harbour Vale Works in 1999, Daniel Pryce has previ&shy;ously been employed in senior posi&shy;tions with:</p>
    <ul>
      <li>- KRM</li>
      <li>- Ashdown New Town Development Corporation</li>
      <li>- Norvale plc</li>
      <li>- Fenwick Estates</li>
    </ul>
    <a class="btn" href="#">Read More</a>
  </section>

  <section class="contact">
    <h2 class="section-title">CONTACT US</h2>
    <address>
      Harbour Vale Works Ltd<br>PO Box 4172<br>Marlbrook<br>MB12 4QT
      <div class="lines">T: 0700 900 4821<br>E: danielp@harbour-vale-works.co.uk</div>
    </address>
  </section>

  <section class="featured">
    <h2 class="section-title">FEATURED PROJECTS</h2>
    <a class="view-more" href="#">View More</a>
    <div class="project-strip">
      <div class="project-thumb thumb-1" role="img" aria-label="Project photo: lattice sculpture in a park"></div>
      <div class="project-thumb thumb-2" role="img" aria-label="Project photo: white apartment block by a lake"></div>
      <div class="project-thumb thumb-3" role="img" aria-label="Project photo: glass and timber office building"></div>
      <div class="project-thumb thumb-4" role="img" aria-label="Project photo: red brick retail building"></div>
      <div class="project-thumb thumb-5" role="img" aria-label="Project photo: white housing across a waterside"></div>
      <div class="project-thumb thumb-6" role="img" aria-label="Project photo: brick apartment tower with balconies"></div>
      <div class="project-thumb thumb-7" role="img" aria-label="Project photo: red brick mansion block"></div>
    </div>
  </section>

  <footer class="copyright">Copyright © 2014 Harbour Vale Works Ltd | All Rights Reserved</footer>
</body>
</html>
```